Marigold Shore Realty business card design

Looking for an upscale and clean business card design and updated logo. I sell to a very high-end south Florida real estate market.
Target Market(s)
High-end real estate in south Florida real estate market
Industry/Entity Type
Real Estate Agent
Contact Information for Business Card
Marigold Shore Realty, Inc
738 West Penrick Ave, Suite 400/500, Fort Lauderdale, FL 33315
Tim Harlow - Broker/Owner
954-327-8846 Direct
timshomes@quillmail.net
Website: StayPenrickAv.net
Font styles to use
Other font styles liked:
- Copperplate Gothic, Georgia, etc.
Requirements
Must have
- My photo, company name, my name and title, all info stated in Details above
Nice to have
- Luxury home design element, waterfront

```html
<!DOCTYPE html>
<html lang="en">
<head>
<meta charset="utf-8">
<title>Marigold Shore Realty – Business Card</title>
<link rel="stylesheet" href="https://fonts.googleapis.com/css2?family=Archivo+Black&family=Arimo:wght@400&family=Gelasio:wght@400&display=swap">
<style>
  :root {
    --page-bg: #2b2b2d;
    --card-black: #050505;
    --card-white: #ffffff;
    --marigold: #f4c430;
    --slate: #4a4a4a;
    --ink: #2a2a2a;
    --rule: #6a6a6a;
    --photo-a: #c9b8a8;
    --photo-b: #2e3f7a;
  }
  * { margin: 0; padding: 0; box-sizing: border-box; }
  html, body { width: 1200px; height: 900px; overflow: hidden; }
  body { background: var(--page-bg); position: relative; font-family: "Arimo", Arial, sans-serif; }

  .card {
    position: absolute;
    width: 620px;
    height: 354px;
    border-radius: 22px;
    overflow: hidden;
  }

  /* Front */
  .card-front {
    left: 60px; top: 60px;
    background: radial-gradient(ellipse at 75% 30%, #1a1a1a 0%, var(--card-black) 65%);
  }
  .front-brand {
    position: absolute; left: 110px; top: 130px;
    display: flex; align-items: center; gap: 22px;
  }
  .brand-dot {
    width: 86px; height: 86px; border-radius: 50%;
    background: var(--marigold);
    flex: none;
  }
  .front-name {
    font-family: "Gelasio", Georgia, serif;
    color: #ffffff;
    font-size: 30px; line-height: 1.15; letter-spacing: 1px;
  }

  /* Back */
  .card-back { left: 520px; top: 486px; background: var(--card-white); }
  .name-bar {
    position: absolute; left: 0; top: 108px;
    width: 345px; height: 62px;
    background: var(--slate);
    border-radius: 0 31px 31px 0;
  }
  .photo-strip {
    position: absolute; left: 0; top: 108px;
    width: 70px; height: 100px; background: var(--slate);
  }
  .person-name {
    position: absolute; left: 178px; top: 114px;
    font-family: "Archivo Black", "Arial Black", sans-serif;
    color: var(--marigold); font-size: 21px; letter-spacing: .3px;
  }
  .person-title {
    position: absolute; left: 178px; top: 142px;
    color: #ffffff; font-size: 16px;
  }
  .portrait {
    position: absolute; left: 40px; top: 104px;
    width: 132px; height: 132px; border-radius: 50%;
    border: 5px solid #ffffff;
    background: linear-gradient(160deg, var(--photo-a) 0%, #e6d5cf 45%, var(--photo-b) 100%);
    box-shadow: 0 0 0 2px var(--slate);
  }
  .back-brand {
    position: absolute; left: 372px; top: 38px;
    display: flex; align-items: center; gap: 10px;
  }
  .back-brand .brand-dot { width: 44px; height: 44px; }
  .back-brand-name {
    font-family: "Gelasio", Georgia, serif;
    color: var(--ink); font-size: 13px;
  }
  .rule { position: absolute; height: 1px; background: var(--rule); }
  .rule-top { left: 360px; top: 132px; width: 240px; }
  .rule-bottom { left: 30px; top: 252px; width: 280px; }
  .address {
    position: absolute; right: 22px; top: 142px;
    text-align: right; color: var(--ink); font-size: 14px; line-height: 1.4;
    white-space: nowrap;
  }
  .contact-list { position: absolute; left: 30px; top: 258px; list-style: none; }
  .contact-list li {
    display: flex; align-items: center; gap: 10px;
    color: var(--ink); font-size: 17px; height: 21px;
    white-space: nowrap;
  }
  .contact-list svg { width: 16px; height: 16px; flex: none; }
  .web-band {
    position: absolute; left: 0; top: 300px;
    width: 100%; height: 30px; background: var(--marigold);
  }
  .web-address {
    position: absolute; left: 300px; top: 5px;
    color: var(--ink); font-size: 17px; letter-spacing: .5px;
  }
</style>
</head>
<body>

<section class="card card-front" aria-label="Card front">
  <div class="front-brand">
    <span class="brand-dot"></span>
    <p class="front-name">Marigold Shore<br>&nbsp;&nbsp;&nbsp;Realty, Inc.</p>
  </div>
</section>

<section class="card card-back" aria-label="Card back">
  <div class="photo-strip"></div>
  <div class="name-bar"></div>
  <p class="person-name">Tim Harlow</p>
  <p class="person-title">Broker/Owner</p>
  <div class="portrait" role="img" aria-label="Portrait photo of Tim Harlow"></div>

  <div class="back-brand">
    <span class="brand-dot"></span>
    <p class="back-brand-name">Marigold Shore Realty, Inc.</p>
  </div>

  <div class="rule rule-top"></div>
  <p class="address">738 West Penrick Ave, Suite 400/500<br>Fort Lauderdale, FL 33315</p>

  <div class="rule rule-bottom"></div>
  <ul class="contact-list">
    <li>
      <svg viewBox="0 0 16 16" aria-hidden="true"><path fill="#f4c430" d="M3.5 1.5l2.3 2.6-1.3 1.7c.9 2 2.5 3.6 4.5 4.5l1.7-1.3 2.6 2.3-1.4 2.2C7.2 14.8 1.2 8.8 1.3 3z"/></svg>
      954-327-8846 Direct
    </li>
    <li>
      <svg viewBox="0 0 16 16" aria-hidden="true"><rect x="1" y="3" width="14" height="10" rx="1" fill="#f4c430"/><path d="M1.5 3.5L8 9l6.5-5.5" fill="none" stroke="#fff" stroke-width="1.2"/></svg>
      timshomes@quillmail.net
    </li>
  </ul>

  <div class="web-band">
    <p class="web-address">StayPenrickAv.net</p>
  </div>
</section>

</body>
</html>
```